"Tidelark Ministry" needs a logo design that represents a Christian family boating ministry

Mission Statement:
“Providing compassion, care and opportunities to create memories for marginalized groups of society through ocean therapy.”
Bible verse:
Colossians 3:12 – “Therefore, as God’s chosen people, holy and dearly loved, clothe yourselves with compassion, kindness, humility, gentleness and patience.”
Target Market(s)
HOMELESS (who have gone through shelters and are on the road to recovery)
CHURCH GROUPS
INJURED MILITARY VETERANS
YOUTH AT RISK (orphans, human trafficking survivors)
SICKLY (hospitalized who can get out once in a while)
CAREGIVERS (single moms, military spouses caring for injured vets, families of those in prison)
ELDERLY (retirement centers)
SMALL BUSINESS STAFF OUTINGS
SPECIAL EVENTS
Industry/Entity Type
Ministry
Contact Information for Business Card
Captain Glen Marbury @ 555-014-2931
Priscilla Marbury @ 555-018-6457
info@tidelarkministry-example.com
www.tidelarkministry-example.com (not active yet but hopefully, soon)
Requirements
Must have
- Catch-phrase words maybe for back of business card:
- "Tidelark --- Kindness --- Sharing days on the waves"
Nice to have
- Added 2 photo files just for visuals:
- 1 photo is of our boat.
- Other photo is our daughter's artwork on a cooler she made (for father's day gift)...might be nice and fun to incorporate daughter's artwork/inspiration into logo...but not sure if it looks to busy

```html
<!DOCTYPE html>
<html lang="en">
<head>
<meta charset="utf-8">
<title>Tidelark Ministry – Business Card</title>
<link href="https://fonts.googleapis.com/css2?family=Tinos:wght@400;700&display=swap" rel="stylesheet">
<style>
  :root {
    --canvas-bg: #e9e6e1;
    --card-white: #ffffff;
    --ink: #2b2b2b;
    --navy: #2d3192;
    --orange: #f68b1f;
    --divider: #3a3a3a;
    --sky: #06a8e8;
    --deep: #2b379b;
  }
  * { margin: 0; padding: 0; box-sizing: border-box; }
  html, body { width: 900px; height: 1200px; overflow: hidden; }
  body {
    background: var(--canvas-bg);
    position: relative;
    font-family: "Tinos", "Times New Roman", serif;
  }
  .card {
    position: absolute;
    border-radius: 24px;
    overflow: hidden;
  }
  .card-front {
    left: 88px; top: 133px; width: 734px; height: 429px;
    background: var(--card-white);
  }
  .brand {
    position: absolute;
    left: 60px; top: 80px; width: 290px;
    text-align: center;
  }
  .brand-dot {
    width: 130px; height: 130px;
    margin: 0 auto 22px;
    border-radius: 50%;
    background: var(--navy);
  }
  .brand-name {
    font-size: 34px;
    font-weight: 400;
    color: var(--navy);
    letter-spacing: 1px;
    line-height: 1;
  }
  .divider {
    position: absolute;
    left: 366px; top: 92px;
    width: 2px; height: 190px;
    background: var(--divider);
  }
  .contacts {
    position: absolute;
    left: 402px; top: 114px;
  }
  .contact { margin-bottom: 12px; }
  .contact-name {
    font-size: 25px;
    color: var(--ink);
    line-height: 1.1;
  }
  .contact-phone {
    display: flex; align-items: center;
    margin-top: 8px;
    font-size: 19px; font-weight: 700;
    color: var(--navy);
  }
  .phone-icon { width: 28px; height: 28px; margin-right: 10px; }
  .contact-band {
    position: absolute;
    left: 0; top: 365px; width: 734px; height: 43px;
  }
  .band-text {
    position: absolute; top: 0; height: 43px;
    display: flex; align-items: center;
    color: #fff; font-size: 17px;
  }
  .band-email { left: 0; width: 370px; justify-content: center; }
  .band-web { left: 380px; width: 354px; justify-content: center; }
  .card-back {
    left: 82px; top: 631px; width: 733px; height: 428px;
    background: linear-gradient(to bottom, var(--sky) 0%, #0a79c9 45%, var(--deep) 100%);
  }
  .back-circle {
    position: absolute;
    left: 206px; top: 60px;
    width: 320px; height: 320px;
    border-radius: 50%;
    border: 16px solid rgba(255,255,255,0.08);
  }
  .tagline {
    position: absolute;
    left: 0; top: 196px; width: 100%;
    text-align: center;
    color: #fff; font-size: 20.5px;
  }
  .tagline .sep { margin: 0 6px; opacity: 0.9; }
</style>
</head>
<body>
  <section class="card card-front">
    <div class="brand">
      <div class="brand-dot"></div>
      <div class="brand-name">Tidelark Ministry</div>
    </div>
    <div class="divider"></div>
    <div class="contacts">
      <div class="contact">
        <div class="contact-name">Captain Glen Marbury</div>
        <div class="contact-phone">
          <svg class="phone-icon" viewBox="0 0 28 28"><circle cx="14" cy="14" r="12.5" fill="none" stroke="#f68b1f" stroke-width="2"/><path d="M8 12c0-3 3-4 6-4s6 1 6 4l-2.5 .5-.5-2h-6l-.5 2zM9.5 13h9l1 6h-11z" fill="#f68b1f"/><circle cx="14" cy="16" r="1.8" fill="#fff"/></svg>
          555-014-2931
        </div>
      </div>
      <div class="contact">
        <div class="contact-name">Priscilla Marbury</div>
        <div class="contact-phone">
          <svg class="phone-icon" viewBox="0 0 28 28"><circle cx="14" cy="14" r="12.5" fill="none" stroke="#f68b1f" stroke-width="2"/><path d="M8 12c0-3 3-4 6-4s6 1 6 4l-2.5 .5-.5-2h-6l-.5 2zM9.5 13h9l1 6h-11z" fill="#f68b1f"/><circle cx="14" cy="16" r="1.8" fill="#fff"/></svg>
          555-018-6457
        </div>
      </div>
    </div>
    <div class="contact-band">
      <svg width="734" height="43" viewBox="0 0 734 43">
        <rect width="734" height="43" fill="#f68b1f"/>
        <path d="M0 0H335C360 0 350 22 375 36Q388 43 410 43H0Z" fill="#2d3192"/>
      </svg>
      <div class="band-text band-email">info@tidelarkministry-example.com</div>
      <div class="band-text band-web">www.tidelarkministry-example.com</div>
    </div>
  </section>

  <section class="card card-back">
    <div class="back-circle"></div>
    <p class="tagline">Tidelark<span class="sep">≈</span>Kindness<span class="sep">≈</span>Sharing days on the waves</p>
  </section>
</body>
</html>
```